business card for a massage therapy practice named 'Meadow and Willow Massage Studio'

I really need a trendy, yet easy on the eyes business card to complement my logo. Ideally with some gold or rose gold foil work.

My uploaded file of the logo I have in horizontal but I have a vertical version as well. Another color that is used in the website is a blush pink here and there. I'd like to see some trendy tropical leaves in the design.

```html
<!DOCTYPE html>
<html lang="en">
<head>
<meta charset="utf-8">
<title>Meadow and Willow Massage Studio – Business Card</title>
<link rel="stylesheet" href="https://fonts.googleapis.com/css2?family=Arimo:wght@400&family=Dancing+Script:wght@500&family=Montserrat:wght@300;500&display=swap">
<style>
  :root{
    --backdrop:#000;
    --sheet:#fff;
    --ink:#1a1a1a;
    --label:#222;
    --rose:#d98c7c;
    --rose-light:#eab3a8;
    --gold:#c9a36a;
    --gold-foil:#e0b56a;
    --mint:#7fd3bf;
    --leaf:#5fb08a;
    --leaf-dark:#2f8a5e;
    --border:#333;
  }
  *{box-sizing:border-box;margin:0;padding:0}
  html,body{width:1200px;height:1200px;overflow:hidden;background:var(--backdrop)}
  .sheet{position:absolute;left:121px;top:41px;width:958px;height:1118px;background:var(--sheet)}
  .side-label{position:absolute;right:48px;font:400 22px "Arimo",Arial,sans-serif;color:var(--label)}
  .side-label.front{top:18px}
  .side-label.back{top:564px}
  .card{position:absolute;left:47px;width:863px;height:503px;border:1px solid var(--border);overflow:hidden;background:var(--sheet)}
  .card.front{top:48px}
  .card.back{top:594px}

  /* logo lockup */
  .logo{position:absolute;display:flex;align-items:center;gap:14px}
  .logo-dot{width:34px;height:34px;border-radius:50%;background:var(--gold);flex:none}
  .logo-name{font:500 30px/1.15 "Montserrat",Arial,sans-serif;color:var(--ink)}
  .front .logo{left:55px;top:42px}
  .back .logo{left:50%;top:168px;transform:translateX(-50%)}
  .back .logo-name{font-size:36px}

  /* leaf artwork areas */
  .leaves{position:absolute}
  .leaves.top-right{right:0;top:0;width:300px;height:325px;border-radius:0 0 0 75%;
    background:radial-gradient(ellipse at 65% 35%,var(--leaf-dark) 0%,var(--leaf) 35%,rgba(170,215,170,.55) 70%,rgba(255,255,255,0) 100%)}
  .leaves.bottom-left{left:15px;bottom:0;width:350px;height:55px;border-radius:50% 50% 0 0;
    background:linear-gradient(0deg,var(--leaf-dark),rgba(95,176,138,.4))}
  .brush-line{position:absolute;left:170px;right:0;top:286px;height:8px;
    background:linear-gradient(90deg,rgba(234,179,168,0),var(--rose-light) 25%,var(--rose-light))}

  .person{position:absolute;left:55px;top:335px;color:var(--rose)}
  .person-name{font:500 48px/1 "Dancing Script",cursive}
  .person-title{font:300 32px/1.2 "Montserrat",Arial,sans-serif;margin-top:4px}

  .contacts{position:absolute;left:470px;top:338px;list-style:none}
  .contacts li{display:flex;align-items:center;gap:12px;font:400 20px/1 "Arimo",Arial,sans-serif;color:var(--ink);height:24px}
  .contacts li+li{margin-top:10px}
  .contacts li.social{margin-top:26px}
  .icon{width:24px;height:24px;flex:none}

  /* back */
  .foil{position:absolute;left:0;right:0;height:130px;
    background:linear-gradient(180deg,var(--rose-light) 0%,var(--rose-light) 38%,var(--gold-foil) 55%,var(--gold-foil) 100%)}
  .foil.top{top:0}
  .foil.bottom{top:328px;height:175px;
    background:linear-gradient(180deg,var(--gold-foil) 0%,var(--rose-light) 30%,var(--rose-light) 50%,var(--gold-foil) 68%,var(--gold-foil) 100%)}
  .band{position:absolute;left:0;right:0;top:130px;height:198px;background:var(--sheet)}
  .leaves.back-top{left:330px;top:35px;width:200px;height:95px;border-radius:50% 50% 0 0;
    background:radial-gradient(ellipse at 50% 100%,var(--leaf-dark),rgba(95,176,138,.5) 70%,rgba(95,176,138,0))}
  .leaves.back-bottom{left:190px;top:328px;width:440px;height:110px;border-radius:0 0 50% 50%;
    background:radial-gradient(ellipse at 50% 0%,var(--leaf-dark),rgba(95,176,138,.55) 60%,rgba(95,176,138,0))}
  .website{position:absolute;left:0;right:0;top:428px;text-align:center;
    font:400 27px/1 "Arimo",Arial,sans-serif;letter-spacing:.3em;color:var(--ink)}
</style>
</head>
<body>
<main class="sheet">
  <span class="side-label front">FRONT</span>
  <section class="card front" aria-label="Card front">
    <div class="leaves top-right" role="img" aria-label="Watercolour tropical palm and monstera leaves"></div>
    <div class="brush-line"></div>
    <div class="leaves bottom-left" role="img" aria-label="Watercolour palm fronds along the bottom edge"></div>

    <div class="logo">
      <span class="logo-dot"></span>
      <p class="logo-name">Meadow and Willow<br>Massage Studio</p>
    </div>

    <div class="person">
      <p class="person-name">Daniela Moreno</p>
      <p class="person-title">LMT</p>
    </div>

    <ul class="contacts">
      <li>
        <svg class="icon" viewBox="0 0 24 24"><rect width="24" height="24" fill="var(--rose)"/><path d="M8 5l3 3-1.5 2a9 9 0 0 0 4.5 4.5L16 13l3 3-2 2.5C11 18 6 13 5.5 7Z" fill="#fff"/></svg>
        555.014.2736
      </li>
      <li>
        <svg class="icon" viewBox="0 0 24 24"><rect width="24" height="24" fill="var(--rose)"/><g fill="none" stroke="#fff" stroke-width="1.3"><circle cx="12" cy="12" r="7"/><ellipse cx="12" cy="12" rx="3" ry="7"/><path d="M5 12h14M6 8.5h12M6 15.5h12"/></g></svg>
        hello@meadowandwillow.com
      </li>
      <li class="social">
        <svg class="icon" viewBox="0 0 24 24"><rect width="24" height="24" fill="var(--rose)"/></svg>
        @meadowandwillow
      </li>
    </ul>
  </section>

  <span class="side-label back">BACK</span>
  <section class="card back" aria-label="Card back">
    <div class="foil top" role="img" aria-label="Rose gold and gold foil brush strokes"></div>
    <div class="foil bottom" role="img" aria-label="Rose gold and gold foil brush strokes"></div>
    <div class="leaves back-top" role="img" aria-label="Tropical leaves rising behind the logo band"></div>
    <div class="leaves back-bottom" role="img" aria-label="Tropical leaves hanging below the logo band"></div>
    <div class="band"></div>
    <div class="logo">
      <span class="logo-dot"></span>
      <p class="logo-name">Meadow and Willow<br>Massage Studio</p>
    </div>
    <p class="website">www.meadowandwillow.com</p>
  </section>
</main>
</body>
</html>
```